Need Brochure Design For Pizza Restaurant

Need redesign for pizza restaurant. Brochure size is 11 Inches X 17 Inches Roll Fold.

Specifications and original menu will be attached.

Target Market(s)

Those who enjoy Pizza ;)

Industry/Entity Type

Restaurant

Requirements
Must have
• The brochure must be double sided.

Must include important information such as operating hours, telephone number, etc.

The brochure should have a snapshot of a map such as Rovi Charts showing the location of the establishment.

All these information could be found on our Rovi Spots page:
http://charts.rovimapex.ca/charts?hl=en&sugexp=frgbld&gs_nf=1&pq=tz+pizza&cp=9&gs_id=4&xhr=t&q=tz%20pizza%20fort%20mcmurray&bav=on.2,or.r_gc.r_pw.r_qf.,cf.osb&biw=1584&bih=810&um=1&ie=UTF-8&sa=N&tab=il

There should be a place where the receiver can cut out a piece of the menu to get a coupon, like in the original design I attached, in which case, there should not be anything important on the reverse side of the brochure where the cut out is to be made.

Final copy needs to be in PDF and PSD, the latter must be separated into layers for ease of later editing.
Nice to have
• Highlight the importance that the establishment is under new management and recently renovated.

```html
<!DOCTYPE html>
<html lang="en">
<head>
<meta charset="utf-8">
<title>Tz's Pizza Menu</title>
<link rel="stylesheet" href="https://fonts.googleapis.com/css2?family=Oswald:wght@400;500;700&family=Raleway:wght@500;600;700&family=Open+Sans:ital,wght@1,300;1,400&display=swap">
<style>
:root{
  --red:#a51f2b;
  --red-dark:#8e1a24;
  --green:#1f9a5a;
  --green-text:#2aa866;
  --panel-dark:#1b1a1a;
  --panel-right:#262223;
  --paper:#ffffff;
  --ink:#2b2b2b;
  --muted:#8a8a8a;
  --price-dark:#3a3a3a;
  --light:#eaeaea;
}
*{margin:0;padding:0;box-sizing:border-box}
html,body{width:1200px;height:779px;overflow:hidden;background:var(--panel-dark)}
.brochure{position:relative;width:1200px;height:779px;font-family:"Raleway",sans-serif}
.panel{position:absolute;top:0;height:779px}
.panel-menu{left:0;width:398px;background:var(--paper)}
.panel-deals{left:398px;width:399px;background:var(--panel-dark)}
.panel-info{left:797px;width:403px;background:var(--panel-right);border-left:1px solid #3a3536}

/* left menu */
.ribbon{position:absolute;left:14px;width:348px;height:27px;background:var(--red);border-radius:14px 0 0 14px;color:#fff;font-family:"Oswald",sans-serif;font-weight:500;font-size:15px;text-align:right;padding-right:8px;line-height:27px;letter-spacing:.3px}
.ribbon::after{content:"";position:absolute;right:-6px;top:0;width:6px;height:27px;background:var(--red-dark)}
.ribbon-fav{top:18px}
.ribbon-sand{top:458px}
.menu-list{position:absolute;left:6px;width:392px;list-style:none}
.list-fav{top:55px}
.list-sand{top:496px}
.menu-item{display:flex;align-items:flex-start;height:28.7px}
.list-sand .menu-item{height:29.2px}
.menu-text{width:356px;text-align:right}
.menu-name{display:block;font-weight:700;font-size:9.5px;color:var(--ink);letter-spacing:.2px;line-height:11px}
.menu-name.small{font-size:6.5px;line-height:9px}
.menu-desc{display:block;font-family:"Open Sans",sans-serif;font-style:italic;font-weight:300;font-size:6.9px;color:var(--muted);line-height:8px;letter-spacing:-.05px}
.menu-desc.narrow{padding-left:20px}
.price{width:30px;padding-left:8px;padding-top:3px;font-weight:700;font-size:9.5px;color:var(--green);line-height:12px;white-space:nowrap}
.price sup{font-size:6px;vertical-align:1px}

/* combos */
.combos{position:absolute;left:13px;top:18px;width:373px;height:354px;background:var(--red);border-radius:10px 28px 28px 10px;color:#fff}
.combos h2{font-family:"Oswald",sans-serif;font-weight:500;font-size:14px;text-align:center;padding-top:6px;letter-spacing:.3px}
.combo-cols{display:flex;padding:6px 0 0 0}
.combo-col{width:186px}
.combo{display:flex;margin-bottom:9px}
.combo-text{width:130px;text-align:right}
.combo-col.right .combo-text{width:120px;margin-left:10px}
.combo-name{display:block;font-weight:700;font-size:9.5px;line-height:11px;letter-spacing:.3px}
.combo-line{display:block;font-family:"Open Sans",sans-serif;font-style:italic;font-weight:300;font-size:7.5px;line-height:9px}
.combo-price{padding-left:7px;font-weight:700;font-size:10px;line-height:11px;white-space:nowrap}
.combo-price sup{font-size:6.5px;vertical-align:2px}

/* daily */
.daily{position:absolute;left:13px;top:388px;width:373px;height:374px;background:var(--green);border-radius:10px 28px 28px 10px;color:#fff;padding:26px 31px 0 32px}
.day{display:flex;align-items:center;border-bottom:1px dashed rgba(255,255,255,.55);height:37.5px}
.day:first-child{height:61px}
.day:last-child{border:none;height:76px}
.day-name{width:120px;font-weight:500;font-size:13px;letter-spacing:.6px;text-transform:uppercase}
.offers{flex:1}
.offer{display:flex;align-items:center;height:37px}
.offer-text{flex:1;text-align:right;line-height:11px}
.offer-head{display:block;font-weight:700;font-size:12.5px;line-height:14px}
.offer-sub{display:block;font-size:9px;font-weight:500}
.offer-price{width:46px;padding-left:12px;font-weight:700;font-size:10px;color:var(--price-dark);white-space:nowrap}
.offer-price sup{font-size:6.5px;vertical-align:2px}

/* info panel */
.brand{position:absolute;left:44px;top:48px;display:flex;align-items:center;gap:18px}
.brand-dot{width:38px;height:38px;border-radius:50%;background:var(--red)}
.brand-name{font-family:"Oswald",sans-serif;font-weight:700;font-size:56px;color:#fff;letter-spacing:1px;line-height:1}
.address{position:absolute;top:152px;left:0;width:403px;text-align:center;color:var(--light);font-weight:500;font-size:15px;letter-spacing:.5px}
.map{position:absolute;left:22px;top:180px;width:351px;height:215px;background:linear-gradient(135deg,#e4e6e1,#d3d7cf 60%,#c9d6dc)}
.hours{position:absolute;top:418px;left:0;width:403px;text-align:center;color:var(--light);font-family:"Open Sans",sans-serif;font-style:italic;font-weight:300;font-size:16px;line-height:20px}
.phone{position:absolute;top:498px;left:62px;color:#fff;font-family:"Oswald",sans-serif;font-weight:500;display:flex;align-items:baseline;gap:6px;line-height:56px}
.phone-label{font-size:15px}
.phone-number{font-size:44px;letter-spacing:.5px}
.web{position:absolute;top:561px;left:0;width:403px;text-align:center;color:var(--light);font-size:14px;font-weight:500;letter-spacing:.8px}
.coupon{position:absolute;left:25px;top:593px;width:346px;height:152px;border:2px dashed var(--green);text-align:center;color:#fff}
.coupon h3{font-family:"Oswald",sans-serif;font-weight:500;font-size:33px;color:var(--red);line-height:1;margin-top:12px}
.coupon-offer{font-family:"Oswald",sans-serif;font-weight:500;font-size:15px;line-height:20px;margin-top:6px;letter-spacing:.3px}
.coupon-offer .free{color:var(--red);font-size:21px}
.coupon-note{color:var(--green-text);font-weight:600;font-size:14px;margin-top:4px;letter-spacing:.3px}
.coupon-expiry{font-family:"Open Sans",sans-serif;font-style:italic;font-size:8.5px;margin-top:6px;color:var(--light)}
.scissors{position:absolute;right:-8px;bottom:-10px;background:var(--panel-right)}
</style>
</head>
<body>
<div class="brochure">

  <section class="panel panel-menu">
    <h2 class="ribbon ribbon-fav">FAVOURITES</h2>
    <ul class="menu-list list-fav">
      <li class="menu-item"><div class="menu-text"><span class="menu-name">HOT BEEF SANDWICH</span><span class="menu-desc">Shaved meat piled high on bread and smothered in gravy</span></div><span class="price">$7,<sup>50</sup></span></li>
      <li class="menu-item"><div class="menu-text"><span class="menu-name">HOT TURKEY SANDWICH</span><span class="menu-desc">Shaved meat piled high on bread and smothered in gravy</span></div><span class="price">$7,<sup>50</sup></span></li>
      <li class="menu-item"><div class="menu-text"><span class="menu-name">HOT HAMBURGER SANDWICH</span><span class="menu-desc">This is an all time favorite of Tz's. Home made beef patty on bread and smothered with gravy</span></div><span class="price">$7,<sup>50</sup></span></li>
      <li class="menu-item"><div class="menu-text"><span class="menu-name">BLACKENED SALMON</span><span class="menu-desc">Grilled blackened chicken seasoned with our blackened spice</span></div><span class="price">$7,<sup>50</sup></span></li>
      <li class="menu-item"><div class="menu-text"><span class="menu-name">PORK CHOP</span><span class="menu-desc">Grilled pork chips topped with sautéed onions and served with applesauce</span></div><span class="price">$7,<sup>50</sup></span></li>
      <li class="menu-item"><div class="menu-text"><span class="menu-name">LIVER AND ONION</span><span class="menu-desc">Tender beef liver grilled to perfection topped with sautéed onions and smothered in gravy</span></div><span class="price">$7,<sup>50</sup></span></li>
      <li class="menu-item"><div class="menu-text"><span class="menu-name">CHICKEN PARMESAN</span><span class="menu-desc">A breaded chicken breast covered in meat sauce and melted mozzarella cheese</span></div><span class="price">$7,<sup>50</sup></span></li>
      <li class="menu-item"><div class="menu-text"><span class="menu-name">VEAL PARMESAN</span><span class="menu-desc">A breaded veal cutlet covered in meat sauce and melted mozzarella cheese</span></div><span class="price">$7,<sup>50</sup></span></li>
      <li class="menu-item"><div class="menu-text"><span class="menu-name">FISH AND CHIPS</span><span class="menu-desc">Two pieces of cod dipped in our homemade beer batter. Served with tartar sauce</span></div><span class="price">$7,<sup>50</sup></span></li>
      <li class="menu-item"><div class="menu-text"><span class="menu-name">HALF BBQ CHICKEN</span><span class="menu-desc">Our oven roasted chicken is a must try</span></div><span class="price">$7,<sup>50</sup></span></li>
      <li class="menu-item"><div class="menu-text"><span class="menu-name">CHICKEN FINGERS</span><span class="menu-desc">Breaded chicken fingers deep-fried golden served with plum sauce</span></div><span class="price">$7,<sup>50</sup></span></li>
      <li class="menu-item"><div class="menu-text"><span class="menu-name">RACK OF BACK RIBS</span><span class="menu-desc">Tender back of baby back ribs covered in a tangy BBQ sauce</span></div><span class="price">$7,<sup>50</sup></span></li>
      <li class="menu-item"><div class="menu-text"><span class="menu-name">CHICKEN BOWL</span><span class="menu-desc">Fresh garden vegetable stir-fried with chicken in honey garlic sauce. Served on rice or noodles</span></div><span class="price">$7,<sup>50</sup></span></li>
      <li class="menu-item"><div class="menu-text"><span class="menu-name">SEAFOOD BOWL</span><span class="menu-desc">Fresh garden vegetable stir-fried with shrimp and scallop in honey garlic sauce. Served on rice or noodles</span></div><span class="price">$7,<sup>50</sup></span></li>
    </ul>

    <h2 class="ribbon ribbon-sand">SANDWICHES</h2>
    <ul class="menu-list list-sand">
      <li class="menu-item"><div class="menu-text"><span class="menu-name">MONTE CRISTO</span><span class="menu-desc">Ham, turkey and mozzarella cheese served triple-decker style on egg dipped grilled bread</span></div><span class="price">$7,<sup>50</sup></span></li>
      <li class="menu-item"><div class="menu-text"><span class="menu-name small">TZ BRUTE</span><span class="menu-desc narrow">This deli styled sandwich is loaded with salami, pepperoni, smoked ham, mozzarella cheese, onions and pizza sauce served on a sub bun</span></div><span class="price">$7,<sup>50</sup></span></li>
      <li class="menu-item"><div class="menu-text"><span class="menu-name">CLUB HOUSE</span><span class="menu-desc">Triple-decker classic with turkey, bacon, tomato, lettuce, cheddar cheese and mayonnaise</span></div><span class="price">$7,<sup>50</sup></span></li>
      <li class="menu-item"><div class="menu-text"><span class="menu-name">RAGING BEEF SANDWICH</span><span class="menu-desc">A classic beef dip sandwich spiffed up with mushrooms and mozzarella cheese</span></div><span class="price">$7,<sup>50</sup></span></li>
      <li class="menu-item"><div class="menu-text"><span class="menu-name">AVOCADO CHICKEN SANDWICH</span><span class="menu-desc">Avocado, grilled chicken, tomato, lettuce and mayonnaise on a toasted bun</span></div><span class="price">$7,<sup>50</sup></span></li>
      <li class="menu-item"><div class="menu-text"><span class="menu-name">ULTIMATE CLUB</span><span class="menu-desc narrow">This triple decker sandwich is loaded with turkey, bacon, ham, roast beef, lettuce, tomato, cheese and jalapeno mayonnaise</span></div><span class="price">$7,<sup>50</sup></span></li>
      <li class="menu-item"><div class="menu-text"><span class="menu-name">STEAK ON THE BUN</span><span class="menu-desc">As delicious as you'd think</span></div><span class="price">$7,<sup>50</sup></span></li>
      <li class="menu-item"><div class="menu-text"><span class="menu-name">BLT</span><span class="menu-desc">Classic sandwich with bacon, lettuce, tomato and mayonnaise on a toasted bun</span></div><span class="price">$7,<sup>50</sup></span></li>
      <li class="menu-item"><div class="menu-text"><span class="menu-name">DENVER SANDWICH</span><span class="menu-desc">Onions and ham grilled with eggs and cheddar on western toast</span></div><span class="price">$7,<sup>50</sup></span></li>
    </ul>
  </section>

  <section class="panel panel-deals">
    <div class="combos">
      <h2>COMBOS</h2>
      <div class="combo-cols">
        <div class="combo-col left">
          <div class="combo"><div class="combo-text"><span class="combo-name">COMBO 1</span><span class="combo-line">3 X 10" Pizza (Three Toppings)</span><span class="combo-line">2L Pop</span></div><span class="combo-price">$31,<sup>99</sup></span></div>
          <div class="combo"><div class="combo-text"><span class="combo-name">COMBO 2</span><span class="combo-line">3 X 12" Pizza (Three Toppings)</span><span class="combo-line">2L Pop</span></div><span class="combo-price">$31,<sup>99</sup></span></div>
          <div class="combo"><div class="combo-text"><span class="combo-name">COMBO 3</span><span class="combo-line">3 X 14" Pizza (3 Toppings)</span><span class="combo-line">2L Cola</span></div><span class="combo-price">$31,<sup>99</sup></span></div>
          <div class="combo"><div class="combo-text"><span class="combo-name">COMBO 4</span><span class="combo-line">2 X 10" Pizza (Three Toppings)</span><span class="combo-line">Dozen Wings</span><span class="combo-line">2L Pop</span></div><span class="combo-price">$31,<sup>99</sup></span></div>
          <div class="combo"><div class="combo-text"><span class="combo-name">COMBO 5</span><span class="combo-line">2 X 12" Pizza (Three Toppings)</span><span class="combo-line">Dozen Wings</span><span class="combo-line">2L Pop</span></div><span class="combo-price">$31,<sup>99</sup></span></div>
          <div class="combo"><div class="combo-text"><span class="combo-name">COMBO 6</span><span class="combo-line">12" Pizza (Three Toppings)</span><span class="combo-line">Boneless Chicken Wings</span><span class="combo-line">Caesar Salad</span><span class="combo-line">2L Pop</span></div><span class="combo-price">$31,<sup>99</sup></span></div>
          <div class="combo"><div class="combo-text"><span class="combo-name">COMBO 7</span><span class="combo-line">2 X Baked Pasta (Garlic Toasts)</span><span class="combo-line">20 Wings</span><span class="combo-line">2L Pop</span></div><span class="combo-price">$31,<sup>99</sup></span></div>
        </div>
        <div class="combo-col right">
          <div class="combo"><div class="combo-text"><span class="combo-name">COMBO 8</span><span class="combo-line">10" Pizza (Three Toppings)</span><span class="combo-line">Rack of Ribs with Spaghetti</span><span class="combo-line">2L Pop</span></div><span class="combo-price">$31,<sup>99</sup></span></div>
          <div class="combo"><div class="combo-text"><span class="combo-name">COMBO 9</span><span class="combo-line">10" Pizza (Three Toppings)</span><span class="combo-line">Ribs and Chicken with Spaghetti</span><span class="combo-line">2L Pop</span></div><span class="combo-price">$31,<sup>99</sup></span></div>
          <div class="combo"><div class="combo-text"><span class="combo-name">COMBO 10</span><span class="combo-line">10" Pizza (Three Toppings)</span><span class="combo-line">Half BBQ Chicken with Spaghetti</span><span class="combo-line">2L Pop</span></div><span class="combo-price">$31,<sup>99</sup></span></div>
          <div class="combo"><div class="combo-text"><span class="combo-name">COMBO 11</span><span class="combo-line">12" Pizza (Three Toppings)</span><span class="combo-line">2 X Baked Pasta</span><span class="combo-line">2L Pop</span></div><span class="combo-price">$31,<sup>99</sup></span></div>
          <div class="combo"><div class="combo-text"><span class="combo-name">COMBO 12</span><span class="combo-line">10" Pizza (Three Toppings)</span><span class="combo-line">Baked Pasta</span><span class="combo-line">Dozen Wings</span><span class="combo-line">2L Pop</span></div><span class="combo-price">$31,<sup>99</sup></span></div>
          <div class="combo"><div class="combo-text"><span class="combo-name">COMBO 13</span><span class="combo-line">12" Pizza (Three Toppings)</span><span class="combo-line">2 X Bacon Cheese Burgers</span><span class="combo-line">Caesar Salad</span><span class="combo-line">2L Pop</span></div><span class="combo-price">$31,<sup>99</sup></span></div>
        </div>
      </div>
    </div>

    <div class="daily">
      <div class="day"><span class="day-name">Monday</span><div class="offers"><div class="offer"><div class="offer-text"><span class="offer-head">2 For 1</span><span class="offer-sub">Steak With Garlic Shrimp. Prime Rib, Rib-Eye, New York and T-Bone.</span></div><span class="offer-price">$29,<sup>50</sup></span></div></div></div>
      <div class="day"><span class="day-name">Tuesday</span><div class="offers"><div class="offer"><div class="offer-text"><span class="offer-head">2 For 1</span><span class="offer-sub">Baby Back Ribs.</span></div><span class="offer-price">$29,<sup>50</sup></span></div></div></div>
      <div class="day"><span class="day-name">Wednesday</span><div class="offers"><div class="offer"><div class="offer-text"><span class="offer-head">2 For 1</span><span class="offer-sub">Pasta.</span></div><span class="offer-price">$29,<sup>50</sup></span></div></div></div>
      <div class="day"><span class="day-name">Thursday</span><div class="offers"><div class="offer"><div class="offer-text"><span class="offer-head">2 For 1</span><span class="offer-sub">Chicken or Beef Burgers.</span></div><span class="offer-price">$29,<sup>50</sup></span></div></div></div>
      <div class="day"><span class="day-name">Friday</span><div class="offers"><div class="offer"><div class="offer-text"><span class="offer-head">2 For 1</span><span class="offer-sub">Fish and Chips.</span></div><span class="offer-price">$29,<sup>50</sup></span></div></div></div>
      <div class="day"><span class="day-name">Saturday</span><div class="offers"><div class="offer"><div class="offer-text"><span class="offer-head">Kids Under 9 Years</span><span class="offer-sub">Eat FREE With Adult Purchase.</span></div><span class="offer-price">$29,<sup>50</sup></span></div></div></div>
      <div class="day"><span class="day-name">Sunday</span><div class="offers"><div class="offer"><div class="offer-text"><span class="offer-head">2 For 1</span><span class="offer-sub">10" 3 Topping Pizza</span></div><span class="offer-price">$29,<sup>50</sup></span></div><div class="offer"><div class="offer-text"><span class="offer-head">2 For 1</span><span class="offer-sub">12" 3 Topping Pizza</span></div><span class="offer-price">$29,<sup>50</sup></span></div></div></div>
    </div>
  </section>

  <section class="panel panel-info">
    <div class="brand"><span class="brand-dot"></span><span class="brand-name">Tz's Pizza</span></div>
    <p class="address">204-118 Birchwood Ave., Fort Mcmurray, AB</p>
    <div class="map" role="img" aria-label="Street map showing the restaurant location in Fort Mcmurray"></div>
    <p class="hours">Delivery is available<br>Sun. - Wed. : 5pm - 10pm<br>Thur. - Sat. : 5pm - 11pm</p>
    <p class="phone"><span class="phone-label">TEL</span><span class="phone-number">780-555-0142</span></p>
    <p class="web">www.tzpizzafortmcmurray.ca</p>
    <div class="coupon">
      <h3>COUPON</h3>
      <p class="coupon-offer">PURCHASE AMOUNT OVER $45 GET THE <span class="free">FREE</span><br>LASAGNA OR 10" GARLIC FINGER</p>
      <p class="coupon-note">Take out and Delivery only</p>
      <p class="coupon-expiry">Expire Date June - 31 - 2012</p>
      <svg class="scissors" width="26" height="22" viewBox="0 0 26 22" aria-hidden="true">
        <circle cx="5" cy="5" r="3.5" fill="none" stroke="#1f9a5a" stroke-width="2"/>
        <circle cx="5" cy="17" r="3.5" fill="none" stroke="#1f9a5a" stroke-width="2"/>
        <line x1="8" y1="7" x2="24" y2="16" stroke="#1f9a5a" stroke-width="2"/>
        <line x1="8" y1="15" x2="24" y2="6" stroke="#1f9a5a" stroke-width="2"/>
      </svg>
    </div>
  </section>

</div>
</body>
</html>
```